I am looking for a stand-out cover that sings out to new parents. The category is very pastel with limited compelling covers that would make me want to buy a book. This book will be used often in the first 12 months of baby's life - so must be strong enough to sit on the bedside table or on the coffee table to inspire reading. It will be a popular gift - so needs to look credible, "pick-up-able" and loveable.

The Book Title is - The Cradle Compass to Infancy's Opening Seasons: Grounded, Research-Led Methods on Rest, Nourishment, Protection plus Growing Assurance
The Size is - 8.5 x 11 in
Book description to be provided to final design for inclusion
Some examples of book covers in this category attached. Thanks

```html
<!DOCTYPE html>
<html lang="en">
<head>
<meta charset="utf-8">
<title>The Cradle Compass to Infancy's Opening Seasons</title>
<link rel="stylesheet" href="https://fonts.googleapis.com/css2?family=Playfair+Display:wght@900&family=Arimo:wght@400&display=swap">
<style>
  :root {
    --paper: #fcfcfd;
    --navy: #053a71;
    --sky: #2a83bc;
    --gold: #c98d32;
    --ink: #1e3f70;
    --rule: #b9cfe2;
    --dots: #c4ccd6;
    --art-core: #e6eff6;
    --art-mid: #f1f5f9;
    --art-edge: #fafbfc;
  }
  * { margin: 0; padding: 0; box-sizing: border-box; }
  html, body { width: 927px; height: 1200px; overflow: hidden; background: var(--paper); }
  .cover { position: relative; width: 927px; height: 1200px; background: var(--paper); font-family: "Arimo", Arial, sans-serif; }

  .series {
    position: absolute; top: 64px; left: 0; width: 100%;
    display: flex; align-items: center; justify-content: center; gap: 26px;
    color: var(--sky); font-size: 46px; letter-spacing: 3px; line-height: 1;
  }
  .series::before, .series::after {
    content: ""; width: 125px; height: 1px; background: var(--rule);
  }

  .title {
    position: absolute; top: 118px; left: 0; width: 100%;
    text-align: center; color: var(--navy);
    font-family: "Playfair Display", Georgia, serif; font-weight: 900;
    font-size: 150px; line-height: 164px; letter-spacing: -1px;
  }

  .tagline {
    position: absolute; top: 458px; left: 0; width: 100%;
    text-align: center; color: var(--gold);
    font-size: 35px; letter-spacing: 2px; line-height: 1;
  }

  .cover-art {
    position: absolute; left: 246px; top: 545px; width: 430px; height: 430px;
    border-radius: 50%;
    border: 3px dotted var(--dots);
    background: radial-gradient(circle at 50% 52%, var(--art-core) 0%, var(--art-mid) 45%, var(--art-edge) 75%);
  }

  .subtitle-block {
    position: absolute; top: 1011px; left: 0; width: 100%; height: 118px;
    display: flex; flex-direction: column; align-items: center; justify-content: center;
    text-align: center; line-height: 1.3;
  }
  .subtitle-block::before, .subtitle-block::after {
    content: ""; position: absolute; left: 200px; width: 527px; height: 1px; background: var(--rule);
  }
  .subtitle-block::before { top: 0; }
  .subtitle-block::after { bottom: 0; }
  .subtitle-lead { color: var(--sky); font-size: 29px; }
  .subtitle-themes { color: var(--ink); font-size: 29px; }
  .subtitle-themes .accent { color: var(--gold); }
</style>
</head>
<body>
<main class="cover">
  <div class="series">THE</div>
  <h1 class="title">Cradle<br>Compass</h1>
  <p class="tagline">TO INFANCY'S OPENING SEASONS</p>

  <div class="cover-art" role="img" aria-label="Cover illustration: a sleeping newborn wrapped in a soft blanket, circled by small themed icons for rest, feeding, safety and bonding"></div>

  <div class="subtitle-block">
    <p class="subtitle-lead">Grounded, Research-Led Methods on Rest,</p>
    <p class="subtitle-themes">Nourishment, <span class="accent">Protection plus Growing Assurance</span></p>
  </div>
</main>
</body>
</html>
```